Granite Ridge Holdings

I have a real estate investment business.

** I need editable vector files of the final design.

Industry/Entity Type

Real Estate

Contact Information for Business Card

I would like the card to be clear and direct with the company name and contact info. I would prefer not to have a design that is too busy (i.e., with excessive detail) in the business card.

Font styles to use
Sans Serif

Requirements
Must have
• My card must have the following information listed below:
• Company name: Grainite Ridge Holdings LLC
• My name: Daniel Vorsley
• Phone number: (555) 218-9067
• Email address: dtvorsley@mailbox-example.net
• Keywords: “Real Estate Investments”
Nice to have
• I would like to have a design that resembles the characteristics/uses of obsidian stone which resembles something related to strength and resilience. Perhaps something with sharp, sleek color transitions as well.

```html
<!DOCTYPE html>
<html lang="en">
<head>
<meta charset="utf-8">
<title>Grainite Ridge Holdings LLC – Business Card</title>
<link rel="stylesheet" href="https://fonts.googleapis.com/css2?family=Exo+2:wght@600&family=Michroma&family=Arimo:ital,wght@0,700;1,400&display=swap">
<style>
  :root {
    --stone-light: #eef1f1;
    --stone-mid: #d9dedf;
    --stone-shade: #c9cfd1;
    --accent-red: #e4141b;
    --ink: #111111;
    --skyline-top: #3b404b;
    --skyline-bottom: #5d6882;
    --white: #ffffff;
  }
  html, body {
    margin: 0;
    padding: 0;
    width: 1200px;
    height: 720px;
    overflow: hidden;
    background: var(--white);
  }
  .card {
    position: relative;
    width: 1200px;
    height: 720px;
    overflow: hidden;
    background:
      linear-gradient(150deg, transparent 0 18%, rgba(255,255,255,0.55) 18% 30%, transparent 30% 44%, rgba(255,255,255,0.5) 44% 56%, transparent 56% 70%, rgba(255,255,255,0.45) 70% 82%, transparent 82%),
      linear-gradient(180deg, var(--stone-light), var(--stone-mid) 60%, var(--stone-shade));
  }
  .company-name {
    position: absolute;
    top: 82px;
    left: 0;
    width: 1200px;
    margin: 0;
    text-align: center;
    white-space: nowrap;
    font-family: "Exo 2", sans-serif;
    font-weight: 600;
    font-size: 80px;
    line-height: 1;
    letter-spacing: 1px;
    color: var(--accent-red);
  }
  .person-row {
    position: absolute;
    top: 290px;
    left: 0;
    width: 1200px;
    display: flex;
    align-items: center;
  }
  .rule {
    height: 7px;
    background: var(--accent-red);
  }
  .rule--left { width: 107px; }
  .rule--right { flex: 1; }
  .person-name {
    margin: 0 22px 0 18px;
    font-family: "Michroma", sans-serif;
    font-size: 50px;
    line-height: 60px;
    color: var(--ink);
    -webkit-text-stroke: 1.6px var(--ink);
    white-space: nowrap;
  }
  .contact {
    position: absolute;
    top: 373px;
    display: flex;
    align-items: center;
    font-family: "Arimo", sans-serif;
    font-style: italic;
    font-size: 37px;
    color: var(--ink);
    white-space: nowrap;
  }
  .contact--phone { left: 42px; }
  .contact--email { left: 509px; }
  .contact-icon {
    width: 72px;
    height: 72px;
    margin-right: 26px;
    flex: none;
  }
  .skyline {
    position: absolute;
    left: 0;
    bottom: 0;
    width: 1200px;
    height: 185px;
    background: linear-gradient(180deg, var(--skyline-top), var(--skyline-bottom));
  }
  .tagline {
    position: absolute;
    left: 0;
    width: 1200px;
    bottom: 14px;
    margin: 0;
    text-align: center;
    font-family: "Arimo", sans-serif;
    font-weight: 700;
    font-size: 25px;
    color: var(--white);
  }
</style>
</head>
<body>
  <main class="card">
    <h1 class="company-name">Grainite Ridge Holdings LLC</h1>

    <div class="person-row">
      <span class="rule rule--left"></span>
      <p class="person-name">Daniel Vorsley</p>
      <span class="rule rule--right"></span>
    </div>

    <div class="contact contact--phone">
      <svg class="contact-icon" viewBox="0 0 72 72" aria-hidden="true">
        <circle cx="36" cy="36" r="33" fill="var(--white)" stroke="var(--accent-red)" stroke-width="3"/>
        <path d="M22 30 q14 -9 28 0 l-2 5 h-6 l-1 -3 q-6 -2 -10 0 l-1 3 h-6 z" fill="var(--accent-red)"/>
        <path d="M27 36 h18 l3 11 h-24 z" fill="var(--accent-red)"/>
      </svg>
      <span class="contact-text">(555) 218-9067</span>
    </div>

    <div class="contact contact--email">
      <svg class="contact-icon" viewBox="0 0 72 72" aria-hidden="true">
        <circle cx="36" cy="36" r="33" fill="var(--white)" stroke="var(--accent-red)" stroke-width="3"/>
        <rect x="22" y="26" width="28" height="20" fill="var(--accent-red)"/>
        <path d="M22 26 L36 38 L50 26" fill="none" stroke="var(--white)" stroke-width="2"/>
      </svg>
      <span class="contact-text">dtvorsley@mailbox-example.net</span>
    </div>

    <div class="skyline" role="img" aria-label="City skyline silhouette of office towers with lit windows"></div>
    <p class="tagline">“Real Estate Investments”</p>
  </main>
</body>
</html>
```